依頼詳細
商品名は「WHEY PROTEIN ISOLATE」です。一般的なプロテインよりも脂肪・糖質を極力排除しており、高純度のたんぱく質を摂取でき、効率的に引き締まった体を作れるのが特徴になります。

メインユーザーは30~40代。男女比はほぼ1:1です。

現行のものは栄養士またはトレーナーがカウンセリングしてから提供することを想定して、名前・量・飲み方を記載して提供できるようにしています(添付ファイルをご覧下さいませ)。レイアウトやデザインは変えてもいいですが、これらの項目自体は変えないようにお願いいたします。

現行品のシンプルさ・清潔感を保ちつつも、「プレミアム」な印象を持てるものになると嬉しいです。

<例1(フォルテン)>
http://shop.forten.jp/products/list.php?category_id=7
<例2(ネクサリオン)>
https://www.nexarion.jp/sports-nutrition/solid-core-blend/48271605.html

以上、よいご提案をお待ちしております。
ご不明な点がございましたら、お気軽にお問い合せ下さいませ。
記載項目
スタンドアルミパウチ:横218mm×縦340mm(チャック下310mm)
※現行品はシールに印刷して貼っていますが、リニューアル品はパウチに印刷しますので、印刷範囲の指定はございません。
希望イメージ
シンプル 複雑
単色 カラフル
暗い 明るい
日常 高級
遊び心 厳粛
未来的 伝統的
女性的 男性的
希望する色
カラーは白地にエメラルドグリーン(DIC63)でお願いいたします。他の色を追加してもOKです。
納品ファイル
• イラストレーター形式 (.ai)
補足説明
選定後はアウトライン化されているファイルと、されていないファイルの両方をお送り下さい。
パーソナルジムに陳列するプロテインですので…あまりにエステっぽいといいますか、女性的なデザインは好ましくないかと思います。
重ねて申し上げますが、シンプルにお願いいたします。<例>もよくご覧下さいませ。
■ 選んだ理由

他にもいいご提案があり悩みましたが、インストラクション部分のデザインが見やすい点が決め手になりました。

■ 提案者全員のお礼・コメント

たくさんのご提案ありがとうございました。また機会がありましたらぜひよろしくお願い致します。

```html
<!DOCTYPE html>
<html lang="en">
<head>
<meta charset="utf-8">
<title>Whey Protein Isolate – Pouch Label</title>
<link rel="stylesheet" href="https://fonts.googleapis.com/css2?family=Archivo+Black&family=Roboto:wght@400;700&display=swap">
<style>
  :root {
    --emerald: #00a98f;
    --emerald-deep: #00664f;
    --emerald-light: #45dcae;
    --ink: #222;
    --rule: #444;
    --paper: #ffffff;
  }
  * { margin: 0; padding: 0; box-sizing: border-box; }
  html, body { width: 846px; height: 1200px; overflow: hidden; background: var(--paper); }
  .pouch { position: relative; width: 846px; height: 1200px; background: var(--paper); font-family: "Roboto", sans-serif; color: var(--ink); }

  .swatch { position: absolute; left: 10px; top: 8px; width: 100px; height: 72px; background: var(--emerald); }
  .swatch-label { position: absolute; left: 12px; top: 84px; font-size: 17px; letter-spacing: 0.5px; color: #555; }

  .trim-marks { position: absolute; inset: 0; pointer-events: none; }

  .title { position: absolute; left: 0; width: 846px; text-align: center; font-family: "Archivo Black", sans-serif; line-height: 1;
    background: linear-gradient(180deg, var(--emerald-light) 0%, var(--emerald) 55%, var(--emerald-deep) 100%);
    -webkit-background-clip: text; background-clip: text; color: transparent;
    -webkit-text-stroke: 3px var(--emerald-deep); }
  .title-whey { top: 196px; font-size: 140px; letter-spacing: 2px; }
  .title-protein { top: 318px; font-size: 134px; letter-spacing: 1px; transform: scaleX(0.96); }
  .title-isolate { top: 440px; font-size: 62px; letter-spacing: 1px; -webkit-text-stroke: 2px var(--emerald-deep); }

  .tagline { position: absolute; top: 508px; left: 0; width: 846px; text-align: center; color: var(--emerald); font-weight: 700; font-size: 14.5px; line-height: 21px; }

  .instructions { position: absolute; left: 322px; top: 588px; width: 214px; font-size: 12.5px; }
  .field { height: 21.6px; border-bottom: 1px solid var(--rule); display: flex; align-items: flex-end; padding-bottom: 3px; }
  .field.heading { font-weight: 700; font-size: 11px; }
  .field.name { height: 34px; font-weight: 700; font-size: 11px; align-items: flex-start; padding-top: 2px; }
  .option { padding-left: 22px; gap: 8px; }
  .box { width: 11px; height: 11px; border: 1px solid var(--ink); display: inline-block; flex: none; margin-bottom: 1px; }
  .blank { flex: 1; display: flex; justify-content: space-between; padding-right: 20px; }

  .brand-band { position: absolute; left: 0; top: 930px; width: 846px; height: 128px; background: var(--emerald); display: flex; align-items: center; justify-content: center; gap: 12px; }
  .brand-mark { width: 16px; height: 16px; border-radius: 50%; background: var(--paper); }
  .brand-name { font-family: "Archivo Black", sans-serif; font-size: 34px; letter-spacing: 3px; color: var(--paper); }
</style>
</head>
<body>
<div class="pouch">
  <div class="swatch"></div>
  <div class="swatch-label">DIC63</div>

  <svg class="trim-marks" width="846" height="1200" viewBox="0 0 846 1200" stroke="#555" stroke-width="1" fill="none">
    <path d="M50 115 H105 M80 90 V140"/>
    <path d="M796 115 H741 M766 90 V140"/>
    <path d="M50 1085 H105 M80 1110 V1060"/>
    <path d="M796 1085 H741 M766 1110 V1060"/>
    <path d="M423 90 V140 M398 115 H448"/>
    <path d="M423 1060 V1110 M398 1085 H448"/>
    <path d="M40 600 H90 M65 575 V625"/>
    <path d="M806 600 H756 M781 575 V625"/>
  </svg>

  <div class="title title-whey">WHEY</div>
  <div class="title title-protein">PROTEIN</div>
  <div class="title title-isolate">ISOLATE</div>

  <p class="tagline">The future you is built from what you eat today.<br>The only way to realize your dream<br>is to keep taking one small step at a time.</p>

  <div class="instructions">
    <div class="field name">Name</div>
    <div class="field heading">Drink</div>
    <div class="field option"><span class="box"></span>WATER &nbsp;/ <span class="box"></span>MILK</div>
    <div class="field heading">Recommended intake per once</div>
    <div class="field option"><span class="box"></span>2 SPOON / 200cc</div>
    <div class="field option"><span class="box"></span>3 SPOON / 300cc</div>
    <div class="field option"><span class="box"></span>4 SPOON / 400cc</div>
    <div class="field option"><span class="box"></span><span class="blank"><span>(</span><span>)</span></span></div>
    <div class="field heading">Recommended timing</div>
    <div class="field option"><span class="box"></span>BREAKFAST</div>
    <div class="field option"><span class="box"></span>AFTER EXERCIZE</div>
    <div class="field option"><span class="box"></span>BEFORE SLEEP</div>
    <div class="field option"><span class="box"></span><span class="blank"><span>(</span><span>)</span></span></div>
  </div>

  <div class="brand-band">
    <span class="brand-mark"></span>
    <span class="brand-name">VELMORA</span>
  </div>
</div>
</body>
</html>
```